Design for Screen Wash Tablet Tube New product

I have a tube which holds screenwash tablets which I need Label created for... Label is 90mm x 90mm. It must include
> logo attached,
>the catchphrase ( drop,dissolve,wash. )
>6 Tablets inside
>1 Tablet makes 5 litres screen wash
>Room for ingredients section( around 20 words)
> Caution - Harmful if swallowed. May cause skin Irritation or eye damage. Do not eat,drink or smoke when using this product. If medical advice is needed have product packaging to hand. Store in a clean dry place.
>Keep out of reach of Children
>Barcode area
>Directions of use
Place tablet in Screenwash bottle
Simply add water
>Product will take approximately 5-10 minutes to fully dissolve.
>3 harmful logo attached
>Cherry Fragrance
Target Market(s)
retail sector - grocery fmcg and car/auto stores
Industry/Entity Type
car care

```html
<!DOCTYPE html>
<html lang="en">
<head>
<meta charset="utf-8">
<title>ClearMist Screen Wash Tablets – Tube Label</title>
<link rel="stylesheet" href="https://fonts.googleapis.com/css2?family=Montserrat:wght@400;500;600;700;800&family=Archivo+Black&display=swap">
<style>
  :root {
    --sky: #109ddb;
    --sky-light: #e6f4fd;
    --navy: #0a2d5a;
    --deep-teal: #06505c;
    --alert-red: #d42400;
    --hazard-red: #e3131b;
    --brand-red: #e3131b;
    --white: #ffffff;
    --ink: #1a1a1a;
  }
  * { box-sizing: border-box; margin: 0; padding: 0; }
  html, body {
    width: 1200px; height: 900px; overflow: hidden;
    background: var(--white);
    font-family: "Montserrat", sans-serif;
  }
  .label {
    position: absolute; left: 182px; top: 28px;
    width: 836px; height: 836px;
    background: var(--sky);
    box-shadow: 6px 6px 14px rgba(0,0,0,0.18);
    overflow: hidden;
  }
  .label-art { position: absolute; inset: 0; width: 836px; height: 836px; }
  .rotated-text { font-family: "Montserrat", sans-serif; }
  .catchphrase { font-family: "Archivo Black", sans-serif; }

  .ingredients {
    position: absolute; left: 39px; top: 572px; width: 404px;
    color: var(--white); font-size: 14px; line-height: 18px;
    text-align: justify; text-align-last: left; letter-spacing: 0.5px;
  }
  .section-title { font-weight: 700; font-size: 14px; letter-spacing: 0.2px; }

  .caution {
    position: absolute; left: 34px; top: 676px; width: 416px; height: 107px;
    background: var(--white); border: 2px solid var(--alert-red);
    border-radius: 7px; overflow: hidden;
  }
  .caution-title {
    background: var(--alert-red); color: var(--white);
    height: 27px; line-height: 27px; text-align: center;
    font-weight: 600; font-size: 21px;
  }
  .caution-text {
    padding: 5px 4px 0 5px; color: var(--ink);
    font-size: 11.3px; line-height: 15px; white-space: nowrap;
    letter-spacing: -0.1px;
  }

  .directions {
    position: absolute; left: 529px; top: 508px; width: 300px;
    color: var(--white);
  }
  .directions ul { list-style: none; margin-top: 3px; }
  .directions li { font-size: 13.5px; line-height: 20px; letter-spacing: 0.3px; padding-left: 18px; position: relative; white-space: nowrap; }
  .directions li::before {
    content: ""; position: absolute; left: 3px; top: 7px;
    width: 6px; height: 6px; border-radius: 50%; background: var(--white);
  }
  .dissolve-note {
    position: absolute; left: 529px; top: 590px; width: 266px;
    color: var(--white); font-weight: 700; font-size: 14.5px; line-height: 21px;
    text-align: justify; text-align-last: left;
  }

  .hazard {
    position: absolute; width: 40px; height: 40px; background: var(--white);
  }
  .hazard svg { width: 40px; height: 40px; display: block; }
  .hazard--environment { left: 529px; top: 676px; }
  .hazard--irritant { left: 584px; top: 676px; }
  .hazard--corrosive { left: 557px; top: 726px; }

  .barcode-area {
    position: absolute; left: 642px; top: 676px; width: 156px; height: 91px;
    background: var(--white);
  }
  .barcode-area svg { position: absolute; inset: 0; }
  .barcode-area span {
    position: absolute; left: 0; right: 0; top: 38px; text-align: center;
    font-size: 9px; font-weight: 600; color: var(--ink);
  }
  .barcode-area span b { background: var(--white); padding: 0 3px; font-weight: 600; }

  .warning-bar {
    position: absolute; left: 0; bottom: 0; width: 836px; height: 35px;
    background: var(--navy); color: var(--white);
    text-align: center; line-height: 35px;
    font-weight: 700; font-size: 22.5px; letter-spacing: 0.3px;
  }
</style>
</head>
<body>
<main class="label">
  <svg class="label-art" viewBox="0 0 1532 1532">
    <defs>
      <linearGradient id="topBand" x1="0" y1="0" x2="1532" y2="0" gradientUnits="userSpaceOnUse">
        <stop offset="0" stop-color="#05303a"/>
        <stop offset="0.4" stop-color="#2f8aa3"/>
        <stop offset="0.47" stop-color="#62dcf6"/>
        <stop offset="0.8" stop-color="#0b6374"/>
        <stop offset="1" stop-color="#06454f"/>
      </linearGradient>
      <linearGradient id="bottomBand" x1="0" y1="0" x2="1532" y2="0" gradientUnits="userSpaceOnUse">
        <stop offset="0" stop-color="#0b3a55"/>
        <stop offset="0.38" stop-color="#3aaecb"/>
        <stop offset="0.52" stop-color="#6edbf4"/>
        <stop offset="0.75" stop-color="#0d6f7e"/>
        <stop offset="1" stop-color="#06505c"/>
      </linearGradient>
      <linearGradient id="wiperShade" x1="0" y1="0" x2="600" y2="0" gradientUnits="userSpaceOnUse">
        <stop offset="0" stop-color="#034a7b"/>
        <stop offset="0.45" stop-color="#3f7aa3"/>
        <stop offset="1" stop-color="#ffffff" stop-opacity="0"/>
      </linearGradient>
      <radialGradient id="cherryTone" cx="0.5" cy="0.6" r="0.5">
        <stop offset="0" stop-color="#d63a1e"/>
        <stop offset="1" stop-color="#d63a1e" stop-opacity="0"/>
      </radialGradient>
    </defs>

    <!-- fragrance corner -->
    <path d="M0,0 L425,0 L0,290 Z" fill="var(--sky-light)"/>
    <rect x="10" y="10" width="130" height="140" fill="url(#cherryTone)" role="img" aria-label="Cherry fruit illustration"/>

    <!-- upper sweep band -->
    <path d="M0,320 C400,150 900,100 1532,150 L1532,160 C1000,170 500,260 0,465 Z" fill="url(#topBand)"/>
    <!-- central white panel -->
    <path d="M0,465 C500,260 1000,170 1532,160 L1532,692 C1000,700 500,800 0,1045 Z" fill="var(--white)"/>
    <g role="img" aria-label="Windscreen wiper blade illustration">
      <path d="M0,465 C500,260 1000,170 1532,160 L1532,692 C1000,700 500,800 0,1045 Z" fill="url(#wiperShade)"/>
    </g>
    <!-- lower sweep band -->
    <path d="M0,1045 C500,800 1000,700 1532,692 L1532,845 C1000,820 500,880 0,1050 Z" fill="url(#bottomBand)"/>
    <path d="M0,1050 C500,880 1000,820 1532,845 L1532,875 C1000,850 500,910 0,1062 Z" fill="#0b86c8"/>

    <text class="rotated-text" x="0" y="0" transform="translate(172,140) rotate(-34)" text-anchor="middle"
          font-size="38" font-weight="600" fill="var(--navy)">Cherry Fragrance</text>

    <text class="rotated-text" x="0" y="0" transform="translate(298,306) rotate(-22)" text-anchor="middle"
          font-size="54" font-weight="500" fill="var(--white)" letter-spacing="1">6 Tablets inside</text>

    <text class="rotated-text" x="1029" y="425" text-anchor="middle"
          font-size="112" font-weight="800" fill="var(--brand-red)">ClearMist</text>

    <text class="catchphrase" x="0" y="0" transform="translate(1018,686) rotate(-10)" text-anchor="middle"
          font-size="64" fill="var(--navy)" letter-spacing="1">DROP · DISSOLVE · WASH</text>

    <text class="rotated-text" x="0" y="0" transform="translate(1066,822) rotate(-5)" text-anchor="middle"
          font-size="45" font-weight="500" fill="var(--white)" letter-spacing="1">1 Tablet makes 5 litres screen wash</text>
  </svg>

  <section class="directions">
    <h2 class="section-title">DIRECTIONS OF USE :</h2>
    <ul>
      <li>Place tablet in Screenwash bottle</li>
      <li>Simply add water</li>
    </ul>
  </section>
  <p class="dissolve-note">Product will take approximately 5-10 minutes to fully dissolve.</p>

  <section class="ingredients">
    <h2 class="section-title">INGREDIENTS :</h2>
    <p>Lorem ipsum dolor sit amet, consectetuer adipiscing elit, sed diam nonummy nibh euismod tincidunt ut laoreet dolore magna aliquam erat volutpat. Ut wisi enim ad minim veniam</p>
  </section>

  <section class="caution">
    <h2 class="caution-title">CAUTION</h2>
    <p class="caution-text">Harmful if swallowed. May cause skin Irritation or eye damage.<br>Do not eat,drink or smoke when using this product.<br>If medical advice is needed have product packaging to hand.<br>Store in a clean dry place</p>
  </section>

  <div class="hazard hazard--environment" role="img" aria-label="Hazard pictogram: environmental hazard">
    <svg viewBox="0 0 40 40"><path d="M20,3 L37,20 L20,37 L3,20 Z" fill="none" stroke="var(--hazard-red)" stroke-width="3"/><rect x="13" y="13" width="14" height="14" fill="#cfd8de" transform="rotate(45 20 20)" opacity="0.6"/></svg>
  </div>
  <div class="hazard hazard--irritant" role="img" aria-label="Hazard pictogram: irritant">
    <svg viewBox="0 0 40 40"><path d="M20,3 L37,20 L20,37 L3,20 Z" fill="none" stroke="var(--hazard-red)" stroke-width="3"/><path d="M18.3,10 L21.7,10 L21,24 L19,24 Z" fill="#000"/><circle cx="20" cy="28" r="2" fill="#000"/></svg>
  </div>
  <div class="hazard hazard--corrosive" role="img" aria-label="Hazard pictogram: corrosive">
    <svg viewBox="0 0 40 40"><path d="M20,3 L37,20 L20,37 L3,20 Z" fill="none" stroke="var(--hazard-red)" stroke-width="3"/><rect x="13" y="13" width="14" height="14" fill="#cfd8de" transform="rotate(45 20 20)" opacity="0.6"/></svg>
  </div>

  <div class="barcode-area">
    <svg viewBox="0 0 156 91" width="156" height="91"><line x1="0" y1="0" x2="156" y2="91" stroke="#000" stroke-width="0.8"/><line x1="156" y1="0" x2="0" y2="91" stroke="#000" stroke-width="0.8"/></svg>
    <span><b>BARCODE AREA</b></span>
  </div>

  <footer class="warning-bar">KEEP OUT OF REACH OF CHILDREN</footer>
</main>
</body>
</html>
```